Business Card and Letterhead
Business card and letterhead to match existing branding.
Project: Business Card and Letterhead
Business Card and Letterhead -
Creative Brief
Use specific fonts
Gill Sans
Professional
Gregor Lindqvast
Project Director
4817 W. Pellham Court #230 Scottsdale, AZ 85391
glindqvast@brovaneshingle.example
www.brovaneshingle.example

```html
<!DOCTYPE html>
<html lang="en">
<head>
<meta charset="utf-8">
<title>Brovane Shingle Co — Stationery Concept</title>
<link href="https://fonts.googleapis.com/css2?family=Cabin:wght@400;600;700&display=swap" rel="stylesheet">
<style>
  :root{
    --brand-red:#d7252b;
    --ink:#2b2b2b;
    --ink-soft:#6b6b6b;
    --paper:#ffffff;
    --board-top:#5c5c5c;
    --board-bottom:#2c2c2c;
    --label:#cfcfcf;
    --envelope-dark:#1e1e1e;
  }
  *{box-sizing:border-box;margin:0;padding:0}
  html,body{width:1200px;height:427px;overflow:hidden}
  body{
    font-family:"Cabin",sans-serif;
    background:radial-gradient(ellipse at 50% 30%,var(--board-top),var(--board-bottom));
    position:relative;color:var(--ink);
  }
  .piece{position:absolute;background:var(--paper);box-shadow:0 3px 8px rgba(0,0,0,.45)}
  .label{position:absolute;font-size:6px;color:var(--label);text-align:center;letter-spacing:.2px}

  /* brand lockup */
  .brand{display:flex;align-items:center;gap:4px}
  .brand__mark{width:12px;height:12px;background:var(--brand-red);flex:none}
  .brand__name{font-weight:700;color:var(--ink);line-height:1;text-transform:uppercase}
  .brand--light .brand__name{color:var(--paper)}
  .brand--light .brand__mark{background:var(--paper)}

  .concept{position:absolute;left:12px;top:84px}
  .concept .brand__mark{width:26px;height:26px}
  .concept .brand__name{font-size:13px;color:#f2f2f2;width:80px}
  .concept__caption{font-size:7px;color:var(--label);margin-top:6px}

  /* business card */
  .card{left:12px;top:139px;width:79px;height:48px;padding:5px}
  .card .brand__mark{width:6px;height:6px}
  .card .brand__name{font-size:4.5px}
  .card__strip{position:absolute;left:0;bottom:0;width:32px;height:22px;background:var(--brand-red);color:var(--paper);padding:3px;font-size:3px;line-height:1.3}
  .card__strip strong{display:block;font-size:3.6px;font-weight:700}
  .card__contact{position:absolute;right:5px;bottom:5px;font-size:2.6px;line-height:1.5;color:var(--ink-soft);text-align:left}

  /* letterheads */
  .letterhead{top:12px;width:172px;height:380px;padding:12px}
  .letterhead--one{left:136px}
  .letterhead--two{left:313px}
  .letterhead__head{display:flex;justify-content:space-between;align-items:flex-start}
  .letterhead .brand__mark{width:10px;height:10px}
  .letterhead .brand__name{font-size:6px;width:56px}
  .letterhead__contact{font-size:3px;line-height:1.5;color:var(--ink-soft);text-align:right}
  .letterhead__rule{position:absolute;left:12px;right:12px;bottom:16px;height:1px;background:var(--brand-red)}
  .letterhead__footer{position:absolute;left:0;right:0;bottom:8px;font-size:2.8px;color:var(--brand-red);text-align:center}
  .letterhead__band{position:absolute;left:0;right:0;bottom:0;height:16px;background:var(--brand-red);color:var(--paper);font-size:2.8px;text-align:center;padding-top:4px;line-height:1.5}

  /* envelopes */
  .envelope{left:506px;width:190px;height:66px;overflow:hidden}
  .envelope svg{position:absolute;inset:0}
  .envelope .brand{position:absolute;left:50%;top:20px;transform:translateX(-50%)}
  .envelope .brand__mark{width:9px;height:9px}
  .envelope .brand__name{font-size:5px}
  .envelope--dark{top:12px;background:var(--envelope-dark)}
  .envelope--red{top:90px}
  .envelope--plain{top:162px}
  .envelope--front{top:232px;height:104px;padding:10px}
  .envelope--front .brand{position:static;transform:none}
  .envelope__address{font-size:3px;color:var(--ink-soft);line-height:1.5;margin-top:4px}
</style>
</head>
<body>

  <section class="concept">
    <div class="brand"><span class="brand__mark"></span><span class="brand__name">Brovane Shingle Co</span></div>
    <p class="concept__caption">Stationary Concept</p>
  </section>

  <article class="piece card">
    <div class="brand"><span class="brand__mark"></span><span class="brand__name">Brovane Shingle Co</span></div>
    <div class="card__strip"><strong>Gregor Lindqvast</strong>Project Director</div>
    <div class="card__contact">P: 480.555.0142<br>F: 480.555.0143<br>glindqvast@brovaneshingle.example<br>www.brovaneshingle.example</div>
  </article>
  <p class="label" style="left:12px;top:193px;width:79px">Business Card</p>

  <article class="piece letterhead letterhead--one">
    <header class="letterhead__head">
      <div class="brand"><span class="brand__mark"></span><span class="brand__name">Brovane Shingle Co</span></div>
      <div class="letterhead__contact">P: 480.555.0142<br>F: 480.555.0143<br>www.brovaneshingle.example</div>
    </header>
    <div class="letterhead__rule"></div>
    <p class="letterhead__footer">4817 W. Pellham Court #230 Scottsdale, AZ 85391</p>
  </article>
  <p class="label" style="left:136px;top:398px;width:172px">Letterhead Option 1</p>

  <article class="piece letterhead letterhead--two">
    <header class="letterhead__head">
      <div class="brand"><span class="brand__mark"></span><span class="brand__name">Brovane Shingle Co</span></div>
    </header>
    <footer class="letterhead__band">4817 W. Pellham Court #230 Scottsdale, AZ 85391<br>P: 480.555.0142 · glindqvast@brovaneshingle.example</footer>
  </article>
  <p class="label" style="left:313px;top:398px;width:172px">Letterhead Option 2</p>

  <article class="piece envelope envelope--dark">
    <svg width="190" height="66" viewBox="0 0 190 66"><path d="M0 0 L95 40 L190 0" fill="none" stroke="#3a3a3a" stroke-width="1"/></svg>
    <div class="brand brand--light"><span class="brand__mark"></span><span class="brand__name">Brovane Shingle Co</span></div>
  </article>

  <article class="piece envelope envelope--red">
    <svg width="190" height="66" viewBox="0 0 190 66"><path d="M0 0 H190 L95 42 Z" fill="var(--brand-red)"/></svg>
    <div class="brand brand--light" style="top:10px"><span class="brand__mark"></span><span class="brand__name">Brovane Shingle Co</span></div>
  </article>

  <article class="piece envelope envelope--plain">
    <svg width="190" height="66" viewBox="0 0 190 66"><path d="M0 0 L95 42 L190 0" fill="none" stroke="#d9d9d9" stroke-width="1"/></svg>
    <div class="brand" style="top:12px"><span class="brand__mark"></span><span class="brand__name">Brovane Shingle Co</span></div>
  </article>

  <article class="piece envelope envelope--front">
    <div class="brand"><span class="brand__mark"></span><span class="brand__name">Brovane Shingle Co</span></div>
    <p class="envelope__address">4817 W. Pellham Court #230<br>Scottsdale, AZ 85391</p>
  </article>
  <p class="label" style="left:506px;top:342px;width:190px">Envelope Variations</p>

</body>
</html>
```